Verostel business card

Business card for sustainable investment company called "Verostel". Verostel is an exchange platform selling carbon credits between buyers and sellers. Carbon Credits are an environmental commodity for reducing global carbon emissions.

the card should obviously have our logo and the theme should be sustainability/environment mixed with a trading platform.

Contact Information for Business Card

Logo, Name, Title, Phone, Email

Colors
0054AA
0677BA
7BADD7
CADEEF
E8F1F8
0094D4
00A9DD
6FCCEA
C7EBF8
E9F6FB
00AB8E
00BBA5
67D7C9
C6EFE9
E9F9F6
59FF00
82FF00
B8FF75
E3FFCB
F4FFEA

```html
<!DOCTYPE html>
<html lang="en">
<head>
<meta charset="utf-8">
<title>Verostel Business Card</title>
<link rel="stylesheet" href="https://fonts.googleapis.com/css2?family=Raleway:wght@500;600;700&display=swap">
<style>
  :root {
    --page-bg: #ffffff;
    --card-bg: #ffffff;
    --brand-blue: #00A9DD;
    --stripe-blue: #6FCCEA;
    --pale-blue: #C7EBF8;
    --mist-blue: #E9F6FB;
    --ink: #1F3450;
    --on-brand: #ffffff;
  }
  * { margin: 0; padding: 0; box-sizing: border-box; }
  html, body {
    width: 1200px;
    height: 1200px;
    overflow: hidden;
    background: var(--page-bg);
    font-family: "Raleway", sans-serif;
  }
  .business-card {
    position: absolute;
    left: 250px;
    top: 390px;
    width: 700px;
    height: 420px;
    background: var(--card-bg);
    box-shadow: 0 0 12px rgba(0, 0, 0, 0.45);
    overflow: hidden;
  }
  .card-shapes {
    position: absolute;
    inset: 0;
    width: 700px;
    height: 420px;
  }
  .brand-name {
    position: absolute;
    left: 141px;
    top: 104px;
    transform: translateX(-50%);
    color: var(--on-brand);
    font-weight: 700;
    font-size: 37px;
    letter-spacing: 0.5px;
    white-space: nowrap;
  }
  .holder {
    position: absolute;
    right: 47px;
    top: 60px;
    text-align: right;
    color: var(--ink);
  }
  .holder-name {
    font-weight: 600;
    font-size: 35px;
    line-height: 40px;
    padding-bottom: 4px;
    border-bottom: 2px solid var(--ink);
    white-space: nowrap;
  }
  .holder-title {
    margin-top: 8px;
    font-weight: 600;
    font-size: 17px;
    letter-spacing: 0.5em;
    margin-right: -0.5em;
    text-align: center;
  }
  .contact-list {
    position: absolute;
    left: 279px;
    top: 216px;
    list-style: none;
    border-left: 3px solid var(--ink);
    padding-left: 24px;
    height: 106px;
    color: var(--ink);
  }
  .contact-item {
    display: flex;
    align-items: center;
    height: 41px;
    margin-top: -6px;
    font-weight: 500;
    font-size: 26px;
    white-space: nowrap;
  }
  .contact-item:first-child { margin-top: -10px; }
  .contact-icon {
    width: 24px;
    height: 24px;
    margin-right: 14px;
    fill: var(--ink);
    flex: none;
  }
</style>
</head>
<body>
  <div class="business-card">
    <svg class="card-shapes" viewBox="0 0 700 420" aria-hidden="true">
      <polygon points="0,0 400,0 0,420" fill="var(--brand-blue)"/>
      <polygon points="400,0 424,0 24,420 0,420" fill="var(--stripe-blue)"/>
      <polygon points="141,294 274,420 24,420 135,301" fill="var(--mist-blue)"/>
      <polygon points="135,301 247,420 24,420" fill="var(--pale-blue)"/>
    </svg>

    <div class="brand-name">VEROSTEL</div>

    <div class="holder">
      <div class="holder-name">YOUR NAME</div>
      <div class="holder-title">TAGLINE</div>
    </div>

    <ul class="contact-list">
      <li class="contact-item">
        <svg class="contact-icon" viewBox="0 0 24 24" aria-hidden="true">
          <path d="M1 5h22v14H1z M3 7.2v9.8h18V7.2l-9 6.3z M3.6 7h16.8L12 12.9z" fill-rule="evenodd"/>
        </svg>
        yourname@verostel.com
      </li>
      <li class="contact-item">
        <svg class="contact-icon" viewBox="0 0 24 24" aria-hidden="true">
          <path d="M6.6 10.8c1.4 2.8 3.8 5.1 6.6 6.6l2.2-2.2c.3-.3.7-.4 1-.2 1.1.4 2.3.6 3.6.6.6 0 1 .4 1 1V20c0 .6-.4 1-1 1C10.6 21 3 13.4 3 4c0-.6.4-1 1-1h3.5c.6 0 1 .4 1 1 0 1.3.2 2.5.6 3.6.1.3 0 .7-.2 1z"/>
        </svg>
        000-000-0000
      </li>
      <li class="contact-item">
        <svg class="contact-icon" viewBox="0 0 24 24" aria-hidden="true">
          <path d="M12 2C8.1 2 5 5.1 5 9c0 5.2 7 13 7 13s7-7.8 7-13c0-3.9-3.1-7-7-7zm0 9.5a2.5 2.5 0 1 1 0-5 2.5 2.5 0 0 1 0 5z"/>
        </svg>
        32/64 your location
      </li>
    </ul>
  </div>
</body>
</html>
```